Small Machinery Hire Company Needs Coaster Design

Please design an eye catching coaster/sticker to place in local pubs and restaurants. Please use our attached logo and incorporate our rustic earthy feel into the colours. Use the following details. Definite want the focus to be on the logo and phone number.

Would appreciate if it could be multi-purpose as a basic sign as well.

Dry/Wet Hire Available
Ph: 0471629058

(Use FaceBook icon) facebook.com/bramwellkestrelplant2917/

Target Market(s)

At homer DIY-ers. Middle class men who would like to hire a machine to work on their own pride and joy home.

Industry/Entity Type

Construction Company

Font styles to use
Other font styles liked:
• Something that matches the Logo

Colors
fefdec
ec1f27
474747
919191

Requirements
Nice to have
• Preferably a square shape so the it is more multi purpose

```html
<!DOCTYPE html>
<html lang="en">
<head>
<meta charset="utf-8">
<title>Bramwell Kestrel Plant – Coaster</title>
<link href="https://fonts.googleapis.com/css2?family=Arvo:wght@400;700&display=swap" rel="stylesheet">
<style>
  :root {
    --page: #ffffff;
    --cream: #fefdec;
    --tread: #e4e2d2;
    --brand-red: #8e1b1f;
    --ink: #222222;
    --ink-soft: #2e2e2e;
  }
  * { box-sizing: border-box; margin: 0; padding: 0; }
  html, body {
    width: 1200px;
    height: 900px;
    overflow: hidden;
    background: var(--page);
  }
  .canvas {
    position: relative;
    width: 1200px;
    height: 900px;
  }
  .coaster {
    position: absolute;
    left: 160px;
    top: 10px;
    width: 880px;
    height: 880px;
    border-radius: 30px;
    overflow: hidden;
    background: var(--cream);
  }
  .tread-texture {
    position: absolute;
    inset: 0;
    background:
      radial-gradient(ellipse at 20% 25%, var(--tread) 0%, transparent 45%),
      radial-gradient(ellipse at 80% 70%, var(--tread) 0%, transparent 45%),
      radial-gradient(ellipse at 85% 15%, var(--tread) 0%, transparent 35%),
      radial-gradient(ellipse at 15% 85%, var(--tread) 0%, transparent 35%),
      var(--cream);
  }
  .item {
    position: absolute;
    white-space: nowrap;
    transform: translate(-50%, -50%) rotate(-41deg);
  }
  .tagline {
    left: 276px;
    top: 250px;
    font-family: "Arvo", serif;
    font-weight: 700;
    font-size: 40px;
    letter-spacing: 2px;
    color: var(--ink-soft);
  }
  .brand-mark {
    left: 430px;
    top: 390px;
    width: 440px;
    height: 230px;
    background: var(--brand-red);
  }
  .brand-name {
    left: 550px;
    top: 540px;
    font-family: "Arvo", serif;
    font-weight: 700;
    font-size: 41px;
    color: var(--ink);
    text-transform: uppercase;
  }
  .phone {
    left: 610px;
    top: 635px;
    font-family: "Arvo", serif;
    font-weight: 400;
    font-size: 40px;
    color: var(--ink);
  }
</style>
</head>
<body>
  <main class="canvas">
    <section class="coaster">
      <div class="tread-texture" role="img" aria-label="Faint grey tyre tread tracks crossing the cream background"></div>
      <p class="item tagline">Call to hire a loader!</p>
      <div class="item brand-mark" aria-hidden="true"></div>
      <h1 class="item brand-name">Bramwell Kestrel Plant</h1>
      <p class="item phone">+61 471 629 058</p>
    </section>
  </main>
</body>
</html>
```